Print Ad for 2024 Prime Counsel Magazine - Show Us Something Unique!

We need an advertisement for back cover of the Prime Counsel annual publication, which will also be included as a featured ad in the Meridian Quarterly, a widely-read, stylish city magazine.

We have a reputation for our originality, personality, and style and 2024 is no different. We want a design that is clever, stylish, unexpected and/or unique.

The one thing we DO NOT WANT is to look like a traditional law firm. We are NOT stuffy old white men. We skip designs that are boring, traditional, or expected. We separate ourselves in our market by NOT acting like a traditional law firm.

More about us: Dravenport Quillmore and Ashby, LLC provides full-service legal representation to entrepreneurs, individuals, and companies for all of their business, employment and litigation needs.

We have included several different photo options. Please use ONLY ONE in the ad.

BE SURE TO REVIEW THE ATTACHMENTS. WE HAVE INCLUDED OUR ADS FOR PRIOR YEARS, BUT WE WANT A TOTALLY DIFFERENT LOOK THIS YEAR!! PLEASE DO NOT PROVIDE SIMILAR ADS.

Target Market(s)

Small business owners, individuals with employment law issues, entrepreneurs, other attorneys.

Industry/Entity Type

Law

Font styles to use
Serif
Sans Serif
Decorative

Requirements
Must have
• It must use our logo, our photo, and our tag line "The Name is Hard to Remember. The Results are Hard to Forget." 1. Use our full firm name of Jeselskis Brinkerhoff and Joseph, LLC2. Use our logo, attached AND our slogan - "THE NAME IS HARD TO REMEMBER. THE RESULTS ARE HARD TO FORGET." Please review the PDF attachments on the ad specs. The ad must follow the following requirements:• COLOR: Must be provided as CMYK, please convert if necessary. • IMAGES: All images must be precisely 300 dpi, placed at 100% to ensure print quality.• LOGOS: Preferred vector (.eps) format, (acceptable as high-res 300 dpi image).• TEXT: Should be editable within the ad. • PRIME COUNSEL REFERENCES: Please adhere to the attached advertising guidelines regarding the appropriate use of the Prime Counsel name, ad concepts and imagery.
Nice to have
• Highly stylized, memorable, upscale look. We really want to show our personality. We take our work seriously, but we don't take ourselves too seriously.
Should not have
• PLEASE REVIEW UPDATED AD SPECS IN ATTACHMENT! Scales of justice, traditional law firm style, or other design features that are predictable in law firm advertising. We don't like clutter or narrative copy.

```html
<!DOCTYPE html>
<html lang="en">
<head>
<meta charset="utf-8">
<title>Dravenport Quillmore and Ashby – Back Cover Ad</title>
<link href="https://fonts.googleapis.com/css2?family=Anton&family=Fira+Sans:wght@500;600&family=Playfair+Display:ital,wght@1,600&display=swap" rel="stylesheet">
<style>
  :root{
    --navy:#1f2560;
    --navy-deep:#141a4a;
    --green:#10a37f;
    --green-deep:#0c5d58;
    --gold:#e3d62c;
    --white:#ffffff;
    --soft:#c9cde8;
  }
  *{margin:0;padding:0;box-sizing:border-box}
  html,body{width:800px;height:1200px;overflow:hidden;background:#a7a7a7}
  .ad{
    position:relative;width:800px;height:1200px;overflow:hidden;
    background:linear-gradient(160deg,#262c6c 0%,var(--navy) 50%,#1b2159 100%);
    color:var(--white);font-family:"Fira Sans",sans-serif;
  }

  .brand{position:absolute;top:38px;left:40px;display:flex;align-items:center;gap:16px}
  .brand__dot{width:56px;height:56px;border-radius:50%;background:var(--white);flex:none}
  .brand__name{font-size:15px;font-weight:600;line-height:20px;letter-spacing:2.5px;text-transform:uppercase}

  .tagline{position:absolute;top:124px;left:40px;width:720px}
  .tagline__first{display:block;font-family:"Playfair Display",serif;font-style:italic;font-weight:600;font-size:42px;line-height:54px}
  .tagline__second{display:block;font-family:"Anton",sans-serif;font-size:46px;line-height:60px;letter-spacing:.5px;color:var(--gold)}

  .practices{position:absolute;top:264px;left:40px;width:720px;display:flex;justify-content:space-between;align-items:center;font-size:14px;font-weight:600;line-height:18px;letter-spacing:.3px;color:var(--soft)}
  .practices__dot{width:7px;height:7px;border-radius:50%;background:var(--green);flex:none}

  .team-photo{position:absolute;top:325px;left:40px;width:720px;height:400px}
  .team-photo__frame{position:absolute;top:12px;left:12px;width:720px;height:400px;border:2px solid var(--gold)}
  .team-photo__image{
    position:absolute;inset:0;
    background:linear-gradient(180deg,#3b4a7a 0%,#6a6f8c 35%,#2f3a5c 70%,#1c2450 100%);
  }

  .roster{position:absolute;top:762px;left:40px;width:732px;display:flex}
  .attorney{width:146.4px;padding:0 8px 0 12px;border-left:2px dotted var(--green)}
  .attorney__name{height:52px;font-family:"Anton",sans-serif;font-size:20px;line-height:24px;letter-spacing:.3px;color:var(--white)}
  .attorney__honors{margin-top:10px;font-size:12.5px;font-weight:500;line-height:16px;color:var(--soft)}
  .attorney__honors p{margin-bottom:8px}

  .footer{position:absolute;left:0;bottom:0;width:800px;height:160px;background:var(--navy-deep);border-top:4px solid var(--green)}
  .footer__phones{position:absolute;left:40px;top:48px;font-size:14px;line-height:20px;letter-spacing:1.6px;font-weight:500}
  .footer__web{
    position:absolute;left:295px;top:56px;width:210px;height:40px;border-radius:3px;
    background:var(--green);
    display:flex;align-items:center;justify-content:center;font-size:16px;letter-spacing:1.8px;font-weight:600;
  }
  .footer__address{position:absolute;right:40px;top:48px;text-align:right;font-size:14px;line-height:20px;letter-spacing:1.2px;font-weight:500}
</style>
</head>
<body>
<div class="ad">
  <header class="brand">
    <span class="brand__dot"></span>
    <span class="brand__name">Dravenport Quillmore<br>and Ashby, LLC</span>
  </header>

  <h1 class="tagline">
    <span class="tagline__first">The Name is Hard to Remember.</span>
    <span class="tagline__second">THE RESULTS ARE HARD TO FORGET.</span>
  </h1>

  <div class="practices">
    <span>Business Litigation<br>&amp; Dispute Resolution</span>
    <span class="practices__dot"></span>
    <span>Entrepreneurship<br>&amp; Small Business</span>
    <span class="practices__dot"></span>
    <span>Employment<br>&amp; Labor</span>
    <span class="practices__dot"></span>
    <span>Contract and<br>Commercial Law</span>
  </div>

  <div class="team-photo">
    <div class="team-photo__frame"></div>
    <div class="team-photo__image" role="img" aria-label="Group photo of the firm's five attorneys standing together against a city backdrop"></div>
  </div>

  <div class="roster">
    <div class="attorney">
      <div class="attorney__name">Reid<br>Calloway</div>
      <div class="attorney__honors">
        <p>Prime Counsel<br>2019 – 2024</p>
        <p>Rising Stars<br>2014, 2018</p>
      </div>
    </div>
    <div class="attorney">
      <div class="attorney__name">Marla Vennick<br>Ashby</div>
      <div class="attorney__honors">
        <p>Prime Counsel</p>
        <p>Top 25 Women<br>2023-2024</p>
        <p>Top 50 2024</p>
        <p>2018 – 2024</p>
        <p>Rising Stars<br>2013 – 2017</p>
      </div>
    </div>
    <div class="attorney">
      <div class="attorney__name">TJ<br>Quillmore</div>
      <div class="attorney__honors">
        <p>Prime Counsel</p>
        <p>Top 25 Women<br>2023-2024</p>
        <p>Top 50 2024</p>
        <p>2018 – 2024</p>
        <p>Rising Stars<br>2013 – 2017</p>
      </div>
    </div>
    <div class="attorney">
      <div class="attorney__name">Danielle<br>Dravenport</div>
      <div class="attorney__honors">
        <p>Prime Counsel</p>
        <p>Top 25 Women<br>2019,2022-2024</p>
        <p>Top 50 2024</p>
        <p>2015 – 2023</p>
        <p>Rising Stars<br>2011 – 2013</p>
      </div>
    </div>
    <div class="attorney">
      <div class="attorney__name">Nora P.<br>Halvey</div>
      <div class="attorney__honors">
        <p>Rising Stars</p>
        <p>2024</p>
      </div>
    </div>
  </div>

  <footer class="footer">
    <div class="footer__phones">555-014-2290<br>555-014-2291 (Fax)<br>info@dqalegal.com</div>
    <div class="footer__web">www.dqalegal.com</div>
    <div class="footer__address">715 N. Larkspur Avenue<br>Suite 210<br>Fairhaven, OH 43020</div>
  </footer>
</div>
</body>
</html>
```